Eyeglasses company needs Professional packaging design for small shipping box

Update 09/11/18 Looking for Black box with black or white lettering. See new pictures.

Update 09.10.18
The previous color scheme is just not working and we have decided to make things simpler and go with a all black box on the outside. All Black with smaller white lettering. The inside of the box white and possible glasses pattern (see new attachment) white, fun and simple on the inside. Looking for creative saying on sides of box and on the inside top.

Update-Deadline extended.

Hi, We have extended the deadline 1 week. We need more designs, more professional and simple with little bit of cuteness and fun sayings about glasses and vision on the side of the box.

All black box with subtle White lettering will WIN- Looking for Hints of the creative characters and logos. Looking for CLEAN, SIMPLE, A little cute, a little fun, Professional. Business Casual.

I've provided a sample image of the box I'm looking for in the brief, still looking for someone to copy that box and make minor adjustments with hints of creativity.

I really need the dieline template on the submissions because I will use that template to submit to the box company.

We are a new company called VARENT based in Southern California that sells high quality, affordable eyeglasses online. We also replace old prescription lenses with new ones in patients own frame. We need a CUTE FUN box to send the frames to the customer!

Box size is 8 inches x 5 inches x 2 inches

*Important- We're using BOXTRIDGE.COM for our creative boxes. They have requirements. Here is the information from them.

We accept both of those file types, including .PNG. Be sure that all artwork/images are at least 300ppi for best print results. Dieline template- instructions in the link regarding artwork that will help. https://boxtridge.helpnest.example/support/solutions/articles/48100072915-design-setup-and-orientation

Hi there,
Here’s the customizable box template you requested. If you have any questions, or when you’re ready to place an order, drop us a line with your files attached and one of our team members will get back to you in a jiffy.
In the meantime, here’s a brief rundown of the artwork set-up guidelines for working with our templates:
• Files should be in CMYK mode (not RGB).
• Be sure to expand all fonts and text to shapes (vectors)* — no live text, please and thank you.
• Embed all images in the document or send the links for the artwork source files. This will prevent any missing links when we go to press.
• Your designs should have at least a 0.25-inch bleed in areas where the graphic exceeds the dieline.
• Dielines should be on a separate layer, visible to prepress for set up. If they are distracting while you are working on or proofing the file, you can turn off their visibility by using the "eye" icon in the Layers palette.
• Send your file(s) in a format that is readable in Adobe Illustrator CS6. If exporting from Adobe Illustrator Creative Cloud, you can down-save to CS6 in the 'Save As' menu.
When your artwork is finished, please send us an email with the artwork attached. We will review the files and provide you with a custom checkout link to use.
• Pro Tip: We created a handy Adobe Illustrator script that will automatically expand your fonts and increase your text size so that they adhere to our artwork guidelines. Download it here: link
Ready? Set. Design!
We can't wait to see what you create!
Your pals at Boxtridge

Target Market(s)

20-60 yo male and female that wear eyeglasses

Industry/Entity Type

Eyewear

Font styles to use
Serif

Colors
000000
eaeaea
ffffff
aaaaaa
1b1b1b
5c5c5c
fefefe
474747
333333

Requirements
Must have
• Must Have:
• - Must be neutral for both genders but cute is a plus.
• - Attached is a sample box of the exact size and type of shipping box.
• - The shipping box will contain the eyeglass frames and case.
• - The dimensions of the shipping box are 8" x 5" x 2"
• -Looking for all black box with white lettering (photo attached). This is creative open project.
• Our website is under construction. Varenteyewear.com
• Looking for cute fun words on the sides/inside of the box including our name and website.
• Examples
• VARENT
• Varenteyewear.com
• Sight, sealed, delivered
• Eyecharts
• Eyelashes
• Anything eye related!!!
• etc etc.
• Looking for creative words on the side of the box and inside the box.
• Front
• Left
• Back
• Right
• Top
• Bottom
• Interior Top
• Interior Bottom
• - Cute, cool, simple fun designs. Subtle Designs on the inside of the box.
• - I'm trying to simplify a complicated process with doctors, prescriptions, insurance.
• - So a simplified first impression is best.

```html
<!DOCTYPE html>
<html lang="en">
<head>
<meta charset="utf-8">
<title>VARENT shipping box dieline</title>
<link href="https://fonts.googleapis.com/css2?family=Lato:wght@300;400&display=swap" rel="stylesheet">
<style>
  :root {
    --paper: #ffffff;
    --board: #aaaaaa;
    --panel-edge: #c9d1dc;
    --cut-line: #1b1b1b;
    --fold-line: #e0553a;
    --bleed-line: #6cb84a;
    --ink: #ffffff;
    --lash-gold: #f3dfa2;
    --lash-sage: #c6dcc0;
  }
  html, body {
    margin: 0;
    padding: 0;
    width: 1200px;
    height: 1129px;
    overflow: hidden;
    background: var(--paper);
  }
  .dieline { display: block; width: 1200px; height: 1129px; }
  .board { fill: var(--board); }
  .panel-frame { fill: none; stroke: var(--panel-edge); stroke-width: 7; }
  .fold { fill: none; stroke: var(--fold-line); stroke-width: 1.2; }
  .cut { fill: none; stroke: var(--cut-line); stroke-width: 1.3; }
  .cut-paper { fill: var(--paper); stroke: var(--cut-line); stroke-width: 1.3; }
  .bleed { fill: none; stroke: var(--bleed-line); stroke-width: 1; }
  .brand {
    font-family: "Lato", sans-serif;
    font-weight: 300;
    fill: var(--ink);
    text-anchor: middle;
  }
  .site {
    font-family: "Lato", sans-serif;
    font-weight: 400;
    fill: var(--ink);
    text-anchor: middle;
  }
  .lash-art { opacity: 0.9; }
</style>
</head>
<body>
<svg class="dieline" viewBox="0 0 1287 1211" preserveAspectRatio="none" xmlns="http://www.w3.org/2000/svg">
  <defs>
    <linearGradient id="lashTone" x1="0" y1="0" x2="1" y2="0">
      <stop offset="0" stop-color="#f3dfa2"/>
      <stop offset="1" stop-color="#c6dcc0"/>
    </linearGradient>
  </defs>

  <!-- dust flaps (white, outside board) -->
  <rect class="cut-paper" x="162" y="18" width="180" height="145" rx="10"/>
  <rect class="cut-paper" x="945" y="18" width="180" height="145" rx="10"/>
  <rect class="cut-paper" x="162" y="530" width="180" height="145" rx="10"/>
  <rect class="cut-paper" x="945" y="530" width="180" height="145" rx="10"/>

  <!-- board outline -->
  <path class="board" d="M322 0 H965 V138 H1287 V550 H965 V660 H1110 V1211 H180 V660 H322 V550 H0 V138 H322 Z"/>

  <!-- bleed guides -->
  <path class="bleed" d="M328 0 V143 H175 Q10 148 10 200 V500 Q10 540 175 540 M958 0 V143 H1112 Q1277 148 1277 200 V500 Q1277 540 1112 540"/>
  <path class="bleed" d="M330 668 H230 Q187 680 187 720 V1010 L240 1030 Q195 1050 195 1110 Q220 1200 330 1200 M955 668 H1055 Q1098 680 1098 720 V1010 L1045 1030 Q1090 1050 1090 1110 Q1065 1200 955 1200"/>

  <!-- side tuck flaps -->
  <path class="cut" d="M180 167 H38 Q27 167 27 180 V285 L18 295 V395 L27 405 V515 Q27 527 38 527 H180"/>
  <path class="cut" d="M1107 167 H1248 Q1260 167 1260 180 V285 L1270 295 V395 L1260 405 V515 Q1260 527 1248 527 H1107"/>

  <!-- lid ear flaps -->
  <path class="cut" d="M352 680 L240 692 Q207 700 207 735 V990 Q207 1015 240 1020 L352 1040"/>
  <path class="cut" d="M352 1048 L245 1056 Q214 1062 214 1090 Q230 1180 330 1192"/>
  <path class="cut" d="M935 680 L1047 692 Q1080 700 1080 735 V990 Q1080 1015 1047 1020 L935 1040"/>
  <path class="cut" d="M935 1048 L1042 1056 Q1073 1062 1073 1090 Q1057 1180 957 1192"/>

  <!-- handle slots -->
  <rect class="cut" x="335" y="292" width="16" height="108" rx="8"/>
  <rect class="cut" x="936" y="292" width="16" height="108" rx="8"/>

  <!-- fold lines -->
  <path class="fold" d="M345 20 V162 H943 V20 M185 162 V530 M1102 162 V530 M345 530 V675 M943 530 V675 M350 678 H937 M350 1046 H937 M340 1048 V1195 M948 1048 V1195"/>

  <!-- panels -->
  <rect class="panel-frame" x="348" y="18" width="592" height="144"/>
  <rect class="panel-frame" x="192" y="166" width="140" height="360"/>
  <rect class="panel-frame" x="338" y="168" width="609" height="358"/>
  <rect class="panel-frame" x="953" y="166" width="143" height="360"/>
  <rect class="panel-frame" x="341" y="533" width="603" height="140"/>
  <rect class="panel-frame" x="357" y="682" width="574" height="362"/>
  <rect class="panel-frame" x="341" y="1051" width="603" height="140"/>

  <!-- left side panel -->
  <g class="lash-art" role="img" aria-label="Eyelash illustration">
    <path d="M250 222 Q285 248 250 276 L262 276 Q292 248 262 222 Z" fill="url(#lashTone)"/>
  </g>
  <g class="lash-art" role="img" aria-label="Eyelash illustration">
    <path d="M250 416 Q285 442 250 470 L262 470 Q292 442 262 416 Z" fill="url(#lashTone)"/>
  </g>
  <text class="brand" font-size="30" letter-spacing="4" transform="translate(267 350) rotate(-90)">VARENT</text>
  <text class="site" font-size="7" letter-spacing="1" transform="translate(279 350) rotate(-90)">Varenteyewear.com</text>

  <!-- right side panel -->
  <g class="lash-art" role="img" aria-label="Eyelash illustration">
    <path d="M1042 222 Q1007 248 1042 276 L1030 276 Q1000 248 1030 222 Z" fill="url(#lashTone)"/>
  </g>
  <g class="lash-art" role="img" aria-label="Eyelash illustration">
    <path d="M1042 416 Q1007 442 1042 470 L1030 470 Q1000 442 1030 416 Z" fill="url(#lashTone)"/>
  </g>
  <text class="brand" font-size="30" letter-spacing="4" transform="translate(1023 344) rotate(90)">VARENT</text>
  <text class="site" font-size="7" letter-spacing="1" transform="translate(1009 344) rotate(90)">Varenteyewear.com</text>

  <!-- front panel (upside down) -->
  <g class="lash-art" role="img" aria-label="Eyelash illustration">
    <path d="M433 630 Q490 575 550 598 L545 605 Q490 590 440 632 Z M445 600 L550 600 L540 578 L455 578 Z" fill="url(#lashTone)" opacity="0.85"/>
  </g>
  <g class="lash-art" role="img" aria-label="Eyelash illustration">
    <path d="M745 628 Q797 580 853 628 L845 630 Q797 592 752 630 Z M755 600 L850 600 L835 578 L770 578 Z" fill="url(#lashTone)" opacity="0.85"/>
  </g>
  <text class="brand" font-size="34" letter-spacing="6" transform="translate(645 612) rotate(180)">VARENT</text>
  <text class="site" font-size="8" letter-spacing="1" transform="translate(645 583) rotate(180)">Varenteyewear.com</text>

  <!-- lid -->
  <text class="brand" x="643" y="881" font-size="50" letter-spacing="8">VARENT</text>
  <text class="site" x="643" y="907" font-size="13" letter-spacing="1.5">Varenteyewear.com</text>

  <!-- lid front -->
  <g class="lash-art" role="img" aria-label="Eyelash illustration">
    <path d="M433 1102 Q488 1150 543 1102 L536 1098 Q488 1138 440 1098 Z M445 1125 L533 1125 L520 1148 L458 1148 Z" fill="url(#lashTone)" opacity="0.85"/>
  </g>
  <g class="lash-art" role="img" aria-label="Eyelash illustration">
    <path d="M737 1102 Q795 1150 853 1100 L846 1096 Q795 1138 744 1098 Z M750 1125 L840 1125 L828 1148 L762 1148 Z" fill="url(#lashTone)" opacity="0.85"/>
  </g>
  <text class="brand" x="643" y="1130" font-size="31" letter-spacing="5">VARENT</text>
  <text class="site" x="643" y="1148" font-size="9" letter-spacing="1">Varenteyewear.com</text>
</svg>
</body>
</html>
```